I need a business card design for a new company that will be doing consulting work around issues of cultural competency, and diversity and inclusion. I would like the design to be crisp and clear with bold but conservative colors and incorporate shades of blue

Target Market(s)

Small businesses, schools, non-profits

Industry/Entity Type

Consulting

Font styles to use
Serif
Sans Serif

Colors
0c5ba6
6b449b
3276b5
0292cd

Requirements
Must have
• A Morrow Venture (name of company)
• Lemlem Tavish
• CEO
• lemlem@amorrowventure.com
• (215)483-2756

```html
<!DOCTYPE html>
<html lang="en">
<head>
<meta charset="utf-8">
<title>A Morrow Venture — Business Card</title>
<link rel="stylesheet" href="https://fonts.googleapis.com/css2?family=PT+Sans:wght@700&display=swap">
<style>
  :root {
    --deep-blue: #0c5ba6;
    --mid-blue: #3276b5;
    --bright-blue: #0292cd;
    --rule-lavender: #cbc8e4;
    --paper: #ffffff;
  }
  * { margin: 0; padding: 0; box-sizing: border-box; }
  html, body {
    width: 1200px;
    height: 686px;
    overflow: hidden;
    background: var(--paper);
  }
  .card {
    position: relative;
    width: 1200px;
    height: 686px;
    background: var(--paper);
    font-family: "PT Sans", "Trebuchet MS", sans-serif;
    font-weight: 700;
    text-align: center;
  }
  .company-name {
    position: absolute;
    left: 0;
    right: 0;
    top: 86px;
    font-size: 100px;
    line-height: 1;
    font-variant: small-caps;
    letter-spacing: 3px;
    color: var(--bright-blue);
  }
  .initial { color: var(--deep-blue); }
  .rule {
    position: absolute;
    left: 135px;
    width: 934px;
    top: 207px;
    height: 4px;
    background: var(--rule-lavender);
  }
  .person {
    position: absolute;
    left: 0;
    right: 0;
    top: 305px;
    font-size: 72px;
    line-height: 1;
    font-variant: small-caps;
    letter-spacing: 2px;
    color: var(--bright-blue);
  }
  .person .title { color: var(--deep-blue); }
  .contact {
    position: absolute;
    left: 0;
    right: 0;
    display: flex;
    justify-content: center;
    align-items: center;
    gap: 22px;
    font-size: 46px;
    line-height: 1;
    color: var(--mid-blue);
    letter-spacing: 1px;
  }
  .contact-phone { top: 440px; }
  .contact-email { top: 565px; }
  .contact-icon { width: 42px; height: 42px; flex: none; }
</style>
</head>
<body>
  <main class="card">
    <h1 class="company-name"><span class="initial">A</span> <span class="initial">M</span>orrow <span class="initial">V</span>enture</h1>
    <div class="rule"></div>
    <h2 class="person"><span class="initial">L</span>emlem <span class="initial">T</span>avish<span class="title">, CEO</span></h2>

    <p class="contact contact-phone">
      <svg class="contact-icon" viewBox="0 0 42 42" aria-hidden="true">
        <circle cx="21" cy="21" r="21" fill="var(--deep-blue)"/>
        <path d="M14 11c1-1 2.5-1 3.3.2l2.2 3.3c.6.9.4 2-.4 2.7l-1.4 1.2c1.2 2.6 3.1 4.6 5.6 5.8l1.2-1.4c.7-.8 1.9-1 2.8-.4l3.3 2.2c1.2.8 1.2 2.3.2 3.3l-1.6 1.6c-1.4 1.4-3.6 1.6-5.4.6C18.400 27.6 14.400 23.600 11.800 18.200c-.9-1.800-.6-4 .8-5.400z" fill="#ffffff"/>
      </svg>
      <span>(215) 483-2756</span>
    </p>

    <p class="contact contact-email">
      <svg class="contact-icon" viewBox="0 0 42 42" aria-hidden="true">
        <circle cx="21" cy="21" r="21" fill="var(--deep-blue)"/>
        <g transform="rotate(-15 21 21)">
          <rect x="10" y="14" width="22" height="15" rx="1.5" fill="#ffffff"/>
          <path d="M10.5 14.8 21 23l10.5-8.2" fill="none" stroke="var(--deep-blue)" stroke-width="1.6"/>
        </g>
      </svg>
      <span>lemlem@amorrowventure.com</span>
    </p>
  </main>
</body>
</html>
```